Eye catching Stationary Design

Healthcare consultant firm looking for stationary design ( letterhead, envelope and business cards) That’s professional, classy and eye catching . The design should incorporate the logo and the colors of the logo in its design. You can see the logo on our website at www crestmore advisory. net.

```html
<!DOCTYPE html>
<html lang="en">
<head>
<meta charset="utf-8">
<title>Crestmore Advisory Group – Stationery</title>
<link rel="stylesheet" href="https://fonts.googleapis.com/css2?family=Cinzel:wght@400;600&family=Roboto:wght@400;700&display=swap">
<style>
:root{
  --backdrop:#d5d5d9;
  --brand-blue:#0b57ad;
  --brand-cyan:#12a3d8;
  --paper:#ffffff;
  --ink:#222a33;
  --muted:#555b63;
}
*{margin:0;padding:0;box-sizing:border-box}
html,body{width:1200px;height:1041px;overflow:hidden}
body{background:var(--backdrop);position:relative;font-family:"Roboto",Arial,sans-serif;color:var(--ink)}
.piece{position:absolute;overflow:hidden}
.serif{font-family:"Cinzel",Georgia,serif}
.wordmark{font-family:"Cinzel",Georgia,serif;font-weight:600;color:var(--brand-blue);letter-spacing:.04em;line-height:1;white-space:nowrap}

/* footer bands: a thin cyan rule above a solid blue base */
.footer-bands{position:absolute;left:0;right:0;bottom:0}
.footer-bands__rule{height:3px;background:var(--brand-cyan)}
.footer-bands__gap{height:2px;background:var(--paper)}
.footer-bands__base{background:var(--brand-blue)}

/* folder */
.folder{left:165px;top:76px;width:418px;height:541px;background:var(--brand-blue);border-radius:3px}
.folder__spine{position:absolute;left:24px;top:0;width:3px;height:100%;background:rgba(0,0,0,.12)}
.folder__mark{position:absolute;left:0;right:0;top:178px;text-align:center;color:#fff;font-size:38px}
.folder__name{position:absolute;left:0;right:0;top:462px;text-align:center;color:#fff;font-size:13.5px;letter-spacing:.03em}

/* letterhead */
.letterhead{left:615px;top:95px;width:403px;height:523px;background:var(--paper)}
.letterhead__mark{position:absolute;left:32px;top:36px;font-size:17px}
.letterhead__contact{position:absolute;right:29px;top:33px;text-align:right}
.letterhead__name{font-size:8px;font-weight:600;letter-spacing:.02em}
.letterhead__line{font-size:5px;color:var(--muted);margin-top:2px}
.letterhead__line b{color:var(--brand-blue)}
.letterhead .footer-bands__base{height:10px}

/* envelope front */
.envelope{left:132px;top:645px;width:451px;height:196px;background:var(--paper)}
.envelope__brand{position:absolute;left:25px;top:24px;display:flex;align-items:center;gap:8px}
.envelope__mark{font-size:13px}
.envelope__name{font-size:8px;font-weight:600;line-height:1.25}
.envelope__return{position:absolute;left:33px;top:162px;font-size:4.5px;color:var(--muted);line-height:1.3}
.envelope__return::before{content:"";position:absolute;left:-7px;top:0;border-left:3px solid #9aa0a8;border-top:4px solid transparent;border-bottom:4px solid transparent}
.envelope .footer-bands__base{height:10px}

/* envelope back */
.envelope-back{left:615px;top:645px;width:451px;height:196px;background:var(--paper)}
.envelope-back__flap{position:absolute;left:4px;right:4px;top:0;height:60px;background:var(--brand-blue);border-radius:0 0 24px 24px}
.envelope-back__mark{position:absolute;left:0;right:0;top:22px;text-align:center;color:#fff;font-size:11px}

/* business cards */
.card{top:870px;width:167px;height:96px}
.card--front{left:417px;background:var(--paper)}
.card__brand{position:absolute;left:8px;top:26px;width:74px;text-align:center}
.card__mark{font-size:10px}
.card__name{font-size:5.5px;font-weight:600;margin-top:6px;line-height:1.3}
.card__divider{position:absolute;left:86px;top:25px;width:1px;height:40px;background:#c9ccd1}
.card__details{position:absolute;left:97px;top:27px;font-size:3.6px;color:var(--muted);line-height:1.35}
.card__person{font-size:4.6px;font-weight:700;color:var(--brand-blue)}
.card__gap{height:4px}
.card--front .footer-bands__rule{height:2px}
.card--front .footer-bands__gap{height:1px}
.card--front .footer-bands__base{height:4px}
.card--back{left:615px;background:var(--brand-blue);text-align:center;color:#fff}
.card--back .wordmark{color:#fff;font-size:15px;margin-top:30px}
.card--back .card__tag{font-size:6px;margin-top:8px;letter-spacing:.02em}
</style>
</head>
<body>

<section class="piece folder" aria-label="Presentation folder">
  <div class="folder__spine"></div>
  <div class="wordmark folder__mark" style="color:#fff">Crestmore</div>
  <div class="serif folder__name">Crestmore Advisory Group LLC</div>
</section>

<section class="piece letterhead" aria-label="Letterhead">
  <div class="wordmark letterhead__mark">Crestmore</div>
  <div class="letterhead__contact">
    <div class="serif letterhead__name">Crestmore Advisory Group LLC</div>
    <div class="letterhead__line">71 Linden Ave S310, Albany, NY 12207</div>
    <div class="letterhead__line">Tel: (555) 014-2270 · <b>www.crestmoreadvisory.net</b></div>
  </div>
  <div class="footer-bands" aria-hidden="true">
    <div class="footer-bands__rule"></div><div class="footer-bands__gap"></div><div class="footer-bands__base"></div>
  </div>
</section>

<section class="piece envelope" aria-label="Envelope front">
  <div class="envelope__brand">
    <div class="wordmark envelope__mark">Crestmore</div>
    <div class="serif envelope__name">Crestmore Advisory<br>Group LLC</div>
  </div>
  <div class="envelope__return">71 Linden Ave S310<br>Albany, NY 12207</div>
  <div class="footer-bands" aria-hidden="true">
    <div class="footer-bands__rule"></div><div class="footer-bands__gap"></div><div class="footer-bands__base"></div>
  </div>
</section>

<section class="piece envelope-back" aria-label="Envelope back">
  <div class="envelope-back__flap">
    <div class="wordmark envelope-back__mark" style="color:#fff">Crestmore</div>
  </div>
</section>

<section class="piece card card--front" aria-label="Business card front">
  <div class="card__brand">
    <div class="wordmark card__mark">Crestmore</div>
    <div class="serif card__name">Crestmore Advisory<br>Group LLC</div>
  </div>
  <div class="card__divider"></div>
  <div class="card__details">
    <div class="card__person">JORDAN WHITFIELD</div>
    <div>General Manager</div>
    <div class="card__gap"></div>
    <div>Tel: (555) 014-2270</div>
    <div>www.crestmoreadvisory.net</div>
    <div class="card__gap"></div>
    <div>71 Linden Ave S310</div>
    <div>Albany, NY 12207</div>
  </div>
  <div class="footer-bands" aria-hidden="true">
    <div class="footer-bands__rule"></div><div class="footer-bands__gap"></div><div class="footer-bands__base"></div>
  </div>
</section>

<section class="piece card card--back" aria-label="Business card back">
  <div class="wordmark">Crestmore</div>
  <div class="serif card__tag">Crestmore Advisory Group LLC</div>
</section>

</body>
</html>
```